Smogline Atlas

Build a simple scrollable "floating" website - Website should have polished, modern look.
Domain has been bought on NameKettle and website should be setup there.
Project Brief:
https://slides.brindlepost.net/deck/7QxKp2vR9tLm4Wz8Ha3NcYe5Bj6Uf1Gd0SoVi/view?mode=shared
Input Files:
https://www.parcelvault.io/f/k3mr81zq5ex7wd2/BXKTpnLdYv9Qe_hRjG4wFs6ox?dl=0

```html
<!DOCTYPE html>
<html lang="en">
<head>
<meta charset="utf-8">
<title>Smogline Atlas Hong Kong</title>
<link href="https://fonts.googleapis.com/css2?family=Oswald:wght@300;400;500&display=swap" rel="stylesheet">
<style>
:root{
  --teal:#167a83;
  --teal-dark:#0f5f67;
  --orange:#c4461a;
  --navy:#1e3b52;
  --input:#8fdde3;
  --ink:#3a3a3a;
  --white:#ffffff;
  --footer:#1b1b1b;
  --sea:#a9d3ee;
}
*{box-sizing:border-box;margin:0;padding:0}
html,body{width:1200px;height:2799px;overflow:hidden}
body{position:relative;font-family:"Oswald",sans-serif;font-weight:300;color:var(--ink);background:var(--white)}
.abs{position:absolute}

/* hero */
.hero{left:0;top:0;width:1200px;height:597px;background:linear-gradient(180deg,#6f8c96 0%,#9a8a78 35%,#6e5a45 60%,#4a3d30 100%)}
.nav-band{left:0;top:58px;width:1200px;height:64px;background:rgba(20,28,32,.55)}
.brand{left:98px;top:12px;width:150px;height:150px;border-radius:50%;background:var(--teal);border:5px solid var(--white);display:flex;align-items:center;justify-content:center;text-align:center;color:var(--white);font-weight:500;font-size:20px;line-height:1.1;letter-spacing:1px;text-transform:uppercase}
.nav{left:358px;top:58px;height:64px;display:flex;align-items:center;gap:24px;color:var(--white);font-weight:400;font-size:15px;letter-spacing:2px;text-transform:uppercase}
.nav-social{left:832px;top:58px;height:64px;display:flex;align-items:center;gap:10px;color:var(--white);font-weight:400;font-size:12px;letter-spacing:.5px}
.cta{left:931px;top:72px;width:170px;height:36px;background:var(--orange);color:var(--white);font-weight:400;font-size:15px;letter-spacing:2px;display:flex;align-items:center;justify-content:center;text-transform:uppercase}
.title-bar{left:99px;top:528px;width:1002px;height:69px;background:var(--teal);color:var(--white);display:flex;align-items:center;justify-content:center;font-weight:400;font-size:44px;letter-spacing:6px;text-transform:uppercase}
.intro{left:99px;top:597px;width:1002px;height:69px;background:var(--white);box-shadow:0 3px 6px rgba(0,0,0,.25);font-size:15px;line-height:24px;text-align:center;padding:9px 24px;letter-spacing:.4px}

/* features */
.feature{width:260px;text-align:center;color:var(--orange);font-weight:400;font-size:15px;letter-spacing:2.5px;line-height:24px;text-transform:uppercase}
.feature .icon{width:94px;height:94px;border-radius:50%;background:var(--teal);border:4px solid #d9d9d9;margin:0 auto 20px;display:flex;align-items:center;justify-content:center}

/* expedition */
.expedition{left:0;top:961px;width:1200px;height:442px;background:linear-gradient(180deg,#4a5863 0%,#2d4a60 30%,var(--navy) 100%)}
.video{left:528px;top:1021px;width:571px;height:323px;background:linear-gradient(160deg,#9bb6bf 0%,#4b6b45 40%,#5f6b6a 75%,#7f8a86 100%);border:2px solid rgba(255,255,255,.5)}
.play{left:786px;top:1152px}
.exp-card{left:103px;top:1064px;width:485px;height:237px;background:rgba(196,70,26,.92);color:var(--white);padding:32px 40px}
.exp-card h2{font-weight:400;font-size:31px;letter-spacing:5px;text-transform:uppercase;margin-bottom:10px}
.exp-card p{font-size:15px;line-height:23px;letter-spacing:.3px}

/* partners */
.section-title{color:var(--teal);font-weight:400;font-size:31px;letter-spacing:5px;text-transform:uppercase;text-align:center;width:1200px;left:0}
.partner{background:#d7dadd}
.partner.round{border-radius:50%}

/* contact */
.contact-photo{left:0;top:1857px;width:599px;height:453px;background:linear-gradient(180deg,#b7c6d1 0%,#7d8e99 50%,#3f5a6a 100%)}
.contact-panel{left:599px;top:1857px;width:601px;height:453px;background:rgba(22,122,131,.93);color:var(--white);padding:55px 99px 0 99px}
.contact-panel h2{font-weight:400;font-size:31px;letter-spacing:5px;text-transform:uppercase;margin-bottom:14px}
.field{width:403px;height:37px;background:var(--input);color:var(--teal-dark);font-size:12px;padding:9px 8px;margin-bottom:15px;letter-spacing:.5px}
.field.message{height:71px}
.submit{width:403px;height:32px;background:var(--orange);color:var(--white);font-weight:400;font-size:13px;letter-spacing:2px;display:flex;align-items:center;justify-content:center;text-transform:uppercase;margin-top:19px}

/* map */
.map{left:0;top:2310px;width:1200px;height:371px;background:linear-gradient(90deg,var(--sea) 0%,#c7dfe9 40%,#e4e4df 65%,var(--sea) 85%)}

/* footer */
.footer{left:0;top:2681px;width:1200px;height:118px;background:var(--footer)}
.foot-brand{left:102px;top:2697px;width:92px;height:92px;border-radius:50%;background:var(--teal);border:3px solid var(--white);display:flex;align-items:center;justify-content:center;text-align:center;font-weight:500;font-size:11px;line-height:1.1;text-transform:uppercase;color:var(--white)}
.quick-title{left:409px;top:2693px;color:var(--input);font-weight:500;font-size:15px;letter-spacing:3px;text-transform:uppercase}
.quick-links{left:409px;top:2731px;display:grid;grid-template-columns:120px 120px;row-gap:2px;font-size:15px;line-height:24px;letter-spacing:1px;font-weight:400;color:var(--white)}
.foot-social{right:99px;top:2713px;display:flex;gap:12px;color:var(--white);font-weight:400;font-size:13px;letter-spacing:.5px}
.copyright{right:99px;top:2754px;font-size:15px;letter-spacing:1.5px;font-weight:400;color:var(--white)}
</style>
</head>
<body>

<section class="hero abs" role="img" aria-label="Rocky Hong Kong shoreline littered with plastic bottles and cans"></section>
<div class="nav-band abs"></div>
<div class="brand abs">Shoreward<br>Circuit</div>
<nav class="nav abs">
  <span>Trash Sites</span><span>Raw Data</span><span>Expedition</span><span>Supporters</span>
</nav>
<div class="nav-social abs"><span>Ripple</span><span>Snapreel</span></div>
<div class="cta abs">Get in touch</div>
<h1 class="title-bar abs">Smogline Atlas Hong Kong</h1>
<p class="intro abs">Results of the first ever water quality and pollution recording of Hong Kong Islands 80 kilometer coastline. The data was recorded during the 2017 Shoreward Circuit Expedition.</p>

<div class="feature abs" style="left:169px;top:727px">
  <div class="icon"><svg width="46" height="46" viewBox="0 0 46 46" fill="none" stroke="#fff" stroke-width="2"><rect x="8" y="6" width="14" height="12"/><path d="M22 12h10v10"/><path d="M4 30c5-4 9 4 14 0s9 4 14 0 9 4 10 0M4 38c5-4 9 4 14 0s9 4 14 0 9 4 10 0"/></svg></div>
  Water Pollution
</div>
<div class="feature abs" style="left:469px;top:727px">
  <div class="icon"><svg width="46" height="46" viewBox="0 0 46 46" fill="none" stroke="#fff" stroke-width="2"><rect x="10" y="6" width="26" height="34" rx="2"/><rect x="17" y="3" width="12" height="6"/><path d="M15 17h3M21 17h10M15 24h3M21 24h10M15 31h3M21 31h10"/></svg></div>
  Reasearch report by<br>Harbour Open<br>University
</div>
<div class="feature abs" style="left:769px;top:727px">
  <div class="icon"><svg width="46" height="46" viewBox="0 0 46 46" fill="none" stroke="#fff" stroke-width="2"><path d="M17 6h10M20 6v12L10 38h24L24 18V6"/><circle cx="30" cy="10" r="3"/><path d="M14 30h16"/></svg></div>
  Biochemistry Data
</div>

<section class="expedition abs" role="img" aria-label="Dusk view over the sea towards distant hills"></section>
<div class="video abs" role="img" aria-label="Video still of climbers on a green rocky headland above the sea"></div>
<svg class="play abs" width="56" height="64" viewBox="0 0 56 64"><path d="M4 2 L54 32 L4 62 Z" fill="rgba(255,255,255,.85)"/></svg>
<div class="exp-card abs">
  <h2>The Expedition</h2>
  <p>In May 2017 Mara Vellin and Jonas Arke completed the first successful coasteering expedition of Hong Kong Island. In 6 days they climbed, swam, scrambled and hiked the entire coastline, took 51 water samples and mapped 163 trash pollution spots</p>
</div>

<h2 class="section-title abs" style="top:1455px">Our Partners</h2>
<div class="partner abs" style="left:168px;top:1558px;width:275px;height:98px"></div>
<div class="partner round abs" style="left:528px;top:1538px;width:144px;height:144px"></div>
<div class="partner abs" style="left:758px;top:1558px;width:316px;height:98px"></div>
<div class="partner abs" style="left:294px;top:1689px;width:230px;height:106px"></div>
<div class="partner abs" style="left:673px;top:1700px;width:230px;height:86px"></div>

<div class="contact-photo abs" role="img" aria-label="Two hikers with climbing gear on a waterfront promenade, city towers behind"></div>
<form class="contact-panel abs">
  <h2>Contact Form</h2>
  <div class="field">Name</div>
  <div class="field">Phone</div>
  <div class="field">Email</div>
  <div class="field message">Message</div>
  <div class="submit">Submit</div>
</form>

<div class="map abs" role="img" aria-label="Street map of the south side of Hong Kong Island around Stanley"></div>

<footer class="footer abs"></footer>
<div class="foot-brand abs">Shoreward<br>Circuit</div>
<div class="quick-title abs">Quick Links</div>
<div class="quick-links abs"><span>Trash Sites</span><span>Expedition</span><span>Raw Data</span><span>Supporters</span></div>
<div class="foot-social abs"><span>Ripple</span><span>Snapreel</span></div>
<div class="copyright abs">Copyright © 2017 &nbsp;|&nbsp; All Rights Reserved.</div>

</body>
</html>
```